Unternehmen für Ordnung und Sauberkeit am Arbeitsplatz und Produkte zur Produktionsoptimierung benötigt Visitenkarten und Briefpapier
Zielgruppe
Produkte für Ordnung und Sauberkeit am Arbeitsplatz, Organisation von Arbeitsplätzen, Produkte zur Vereinfachung von Arbeitsabläufen, Produkte zur Produktionsoptimierung unter dem Lean Gedanke, Schlagwort: "5S", nachhaltig, sauber
Aufgabenstellung
Wir sind auf der Suche nach Visitenkarten und Briefpapier für das Unternehmen ourKarto. Nachhaltig, Sauber usw.. Unser Firmenlogo finden Sie anbei.

```html
<!DOCTYPE html>
<html lang="de">
<head>
<meta charset="utf-8">
<title>ourKarto – Visitenkarten</title>
<link rel="stylesheet" href="https://fonts.googleapis.com/css2?family=PT+Sans:ital,wght@0,400;0,700;1,700&display=swap">
<style>
  :root {
    --bg: #2a2c2e;
    --card: #f7f7f7;
    --teal: #138f78;
    --green: #2fa383;
    --green-soft: rgba(47, 163, 131, 0.45);
    --grey-soft: rgba(120, 120, 120, 0.35);
    --grey-dark: #3d3d3d;
    --text: #1f1f1f;
  }
  * { margin: 0; padding: 0; box-sizing: border-box; }
  html, body { width: 1163px; height: 1200px; overflow: hidden; }
  body {
    background: var(--bg);
    font-family: "PT Sans", Arial, sans-serif;
    position: relative;
  }
  .card {
    position: absolute;
    width: 692px;
    height: 385px;
    background: radial-gradient(ellipse at 60% 55%, #ffffff 0%, var(--card) 60%, #ececec 100%);
    overflow: hidden;
  }
  .card--front { left: 167px; top: 233px; }
  .card--back  { left: 302px; top: 673px; }

  .wave-area {
    position: absolute;
    width: 420px;
    height: 300px;
  }
  .card--front .wave-area {
    left: 0;
    top: 0;
    background: linear-gradient(150deg, var(--green-soft) 0%, var(--grey-soft) 30%, rgba(255,255,255,0) 60%);
  }
  .card--back .wave-area {
    right: 0;
    bottom: 0;
    background: linear-gradient(330deg, var(--green-soft) 0%, var(--grey-soft) 30%, rgba(255,255,255,0) 60%);
  }

  .brand {
    position: absolute;
    display: flex;
    align-items: center;
    gap: 8px;
    color: var(--grey-dark);
    font-weight: 700;
    letter-spacing: -0.5px;
  }
  .brand__mark { background: var(--green); display: block; }
  .card--front .brand { left: 457px; top: 44px; font-size: 34px; }
  .card--front .brand__mark { width: 40px; height: 40px; }
  .card--back .brand { left: 111px; top: 124px; font-size: 50px; }
  .card--back .brand__mark { width: 62px; height: 62px; }

  .person {
    position: absolute;
    right: 259px;
    top: 180px;
    text-align: right;
  }
  .person__name {
    color: var(--teal);
    font-size: 24px;
    font-weight: 700;
    font-style: italic;
    line-height: 1;
  }
  .person__role { font-size: 15.5px; color: var(--text); margin-top: 8px; }
  .divider {
    position: absolute;
    left: 459px;
    top: 183px;
    width: 3px;
    height: 185px;
    background: var(--teal);
  }
  .contact {
    position: absolute;
    left: 488px;
    top: 183px;
    font-size: 16px;
    line-height: 23px;
    color: var(--text);
  }
  .contact__group + .contact__group { margin-top: 24px; }
  .web-url {
    position: absolute;
    left: 258px;
    top: 214px;
    font-size: 23px;
    font-weight: 700;
    font-style: italic;
    color: var(--grey-dark);
  }
</style>
</head>
<body>

<section class="card card--front">
  <div class="wave-area" role="img" aria-label="Dekorative Wellenbänder in Grün und Grau"></div>

  <div class="brand"><span class="brand__mark"></span>ourKarto</div>

  <div class="person">
    <p class="person__name">Jonas Brenneck</p>
    <p class="person__role">Geschäftsführer</p>
  </div>

  <div class="divider"></div>

  <div class="contact">
    <p class="contact__group">Lindenweg 7<br>79312 Emmendorf</p>
    <p class="contact__group">mail: info@ourkarto.de<br>web: www.ourkarto.de</p>
    <p class="contact__group">tel: 0 31 47 / 20 48 61<br>fax: 0 31 47 / 20 48 619</p>
  </div>
</section>

<section class="card card--back">
  <div class="wave-area" role="img" aria-label="Dekorative Wellenbänder in Grün und Grau"></div>

  <div class="brand"><span class="brand__mark"></span>ourKarto</div>
  <p class="web-url">www.ourkarto.de</p>
</section>

</body>
</html>
```